New Toothpaste brand needs a logo & packaging design

Our company is launching a new toothpaste and is looking for a logo and packaging design. The toothpaste brand is called Brivana. The packaging should have the same design quality as the major international brands, such as Lumora, Lumora Totalcare, Dentiva, Pexolo, Wind-rise, Marvest, etc. The dominant colors for our brand should be hues of blue, similar to other major brands. In addition, there should be a little bit of green to represent the "Fresh Mint Blast" flavor and the "Extracts of Aloe Vera" included in the ingredients.

There are typically 3 unique sides on a toothpaste box:

The face: Repeated on ~3 sides of the 4 faces of the box
The back: The 4th box face has the instructions for use, ingredients, company information, bar code/product info, and some branding elements.
The sides: Usually consisting of just the logo, flavor etc.

Please refer to existing brands such as Lumora, Lumora Total-care, and Dentiva for an example of typical box layout and elements.

Task Details:
Package Dimensions: 180 mm x 48 mm x 28 mm, 100 ml toothpaste tube
Brand Name: Brivana
Description: Fluoride Toothpaste
Flavor: Fresh Mint Blast
5 Actions: Protects against cavities and tartar, freshens breath, whitens teeth, and maintains healthy gums. These actions can also be made into a list like Lumora Total Care or Dentiva Max care. For instance, Strong Teeth, Fresh Breath, Whitening, Healthy Gums, Cavity and Tartar Protection.
Also contains whitening micro particles and extracts of aloe vera which may be highlighted on the package

Overall, the look should be high quality and with the same look and feel as the big brands mentioned previously. We do not have an existing logo for this brand. The face of the package is the most important element as it is often repeated on several sides and on the tube itself.

Please let me know if you have any questions.

I've attached some of our favorite big brand designs below. I would say the Lumora Total Care and Gleam vers

The logos I've seen so far for Brivana, have been a bit too bold. A little bold is okay, but just needs to be moderate. 

I would like the colors to be bright and appealing. I mentioned shades of blue being the major color, but green should also be highlighted as well, perhaps in a 80% blue to 20% green ratio. 

Target Market(s)

adult consumer of toothpaste, both female and male.

Industry/Entity Type

It Company

Requirements
Must have
• A logo with the brand name: Brivana
Description or sub text: Fluoride Toothpaste
Flavor: Fresh Mint Blast
A phrase or list describing the Toothpaste Actions: e.g., Protects against cavities and tartar, freshens breath, whitens teeth, and maintains healthy gums. Or as a list simialr to Lumora Total Care or Dentiva Max Care:
-Anti-cavity
-Anti-tartar
-Fresh breath
-Whitening
-Healthy Gums

Special ingredient of "whitening micro particles: and "extracts of aloe vera", which should also be highlighted.

The color should mostly be shades of blue, with only a little bit of green to accentuate the fresh mint blast flavor and aloe vera

Nice to have
• The design should really look good next to lumora total care, gleam pure, and dentiva max care. These are our favorite designs.
Should not have
• For aloe vera, there is no need to show the plant.

The Brivana logo shouldn't be too Bold. This should be appeal to all consumers, not just men.

```html
<!DOCTYPE html>
<html lang="en">
<head>
<meta charset="utf-8">
<title>Brivana Toothpaste Box – Face Variations</title>
<link href="https://fonts.googleapis.com/css2?family=Montserrat:wght@600;700&display=swap" rel="stylesheet">
<style>
  :root {
    --page-bg: #ffffff;
    --top-bar: #1b75bc;
    --blue-light: #2a6fc4;
    --blue-mid: #2451ad;
    --blue-deep: #2b3596;
    --green: #22a872;
    --green-light: #3cc08c;
    --green-dark: #159a66;
    --red: #e3242b;
    --red-mid: #b3536a;
    --red-fade: #6f70b0;
    --white: #ffffff;
    --silver-light: #f4f6f8;
    --silver-dark: #a9b3bf;
  }
  * { box-sizing: border-box; margin: 0; padding: 0; }
  html, body {
    width: 1200px; height: 1000px; overflow: hidden;
    background: var(--page-bg);
    font-family: "Montserrat", Arial, sans-serif;
  }
  .canvas { position: relative; width: 1200px; height: 1000px; }
  .top-bar { position: absolute; left: 0; top: 0; width: 1200px; height: 8px; background: var(--top-bar); }

  .box-face {
    position: absolute; left: 276px; width: 648px; height: 153px; overflow: hidden;
    background:
      radial-gradient(ellipse at 30% 20%, rgba(120,180,255,.35), transparent 60%),
      linear-gradient(120deg, var(--blue-light) 0%, var(--blue-mid) 50%, var(--blue-deep) 100%);
    color: var(--white);
  }
  .box-face--1 { top: 87px; }
  .box-face--2 { top: 293px; }
  .box-face--3 { top: 505px; }
  .box-face--4 { top: 711px; }

  .brand-name {
    position: absolute; left: 24px; top: 28px;
    font-size: 62px; font-weight: 700; line-height: 1; letter-spacing: -1px;
    color: var(--white);
  }

  .aloe-badge {
    position: absolute; left: 292px; top: 78px; width: 112px; height: 26px;
    background: linear-gradient(90deg, var(--green-dark), var(--green-light));
    display: flex; align-items: center; gap: 5px; padding-left: 5px;
  }
  .aloe-badge__dot { width: 17px; height: 17px; border-radius: 50%; background: var(--white); flex: none; }
  .aloe-badge__text { font-size: 9.5px; font-weight: 700; line-height: 1.05; text-transform: uppercase; }

  .claim-band {
    position: absolute; left: 0; top: 112px; width: 412px; height: 21px;
    background: linear-gradient(90deg, var(--green-dark), var(--green-light));
    font-size: 12.2px; font-weight: 700; line-height: 21px; padding-left: 12px; white-space: nowrap;
  }
  .box-face--3 .claim-band,
  .box-face--4 .claim-band {
    background: linear-gradient(90deg, var(--red) 0%, var(--red-mid) 60%, var(--red-fade) 100%);
  }

  .volume { position: absolute; left: 11px; top: 137px; font-size: 10.5px; font-weight: 600; }

  .mint-strip {
    position: absolute; left: 429px; top: 0; width: 67px; height: 153px;
    background: linear-gradient(180deg, var(--white) 0%, #bfe9d6 35%, var(--green-light) 75%, var(--green) 100%);
  }
  .mint-strip__seal {
    position: absolute; left: 4px; top: 68px; width: 59px; height: 59px; border-radius: 50%;
    border: 4px solid var(--green-light);
    background: radial-gradient(circle at 40% 35%, var(--silver-light), var(--silver-dark));
  }

  .benefit-list {
    position: absolute; left: 530px; top: 13px; list-style: none;
    font-size: 10.4px; font-weight: 700; line-height: 13px; text-transform: uppercase;
  }

  .flavor-band {
    position: absolute; left: 522px; top: 103px; width: 126px; height: 24px;
    background: linear-gradient(90deg, var(--green-dark), var(--green-light));
    font-size: 10.4px; font-weight: 700; line-height: 18px; padding-left: 10px; white-space: nowrap;
  }
</style>
</head>
<body>
<div class="canvas">
  <div class="top-bar"></div>

  <section class="box-face box-face--1">
    <div class="brand-name">Brivana</div>
    <div class="aloe-badge"><span class="aloe-badge__dot"></span><span class="aloe-badge__text">Extracts<br>of Aloe Vera</span></div>
    <div class="claim-band">FLUORIDE TOOTHPASTE WITH WHITENING MICRO PARTICLES</div>
    <div class="volume">100ml</div>
    <div class="mint-strip"><div class="mint-strip__seal" role="img" aria-label="Silver medical seal emblem"></div></div>
    <ul class="benefit-list"><li>Strong Teeth</li><li>Fresh Breath</li><li>Whitening</li><li>Healthy Gums</li><li>Cavity</li><li>Tartar</li></ul>
    <div class="flavor-band">FRESH MINT BLAST</div>
  </section>

  <section class="box-face box-face--2">
    <div class="brand-name">Brivana</div>
    <div class="aloe-badge"><span class="aloe-badge__dot"></span><span class="aloe-badge__text">Extracts<br>of Aloe Vera</span></div>
    <div class="claim-band">FLUORIDE TOOTHPASTE WITH WHITENING MICRO PARTICLES</div>
    <div class="volume">100ml</div>
    <div class="mint-strip"><div class="mint-strip__seal" role="img" aria-label="Silver medical seal emblem"></div></div>
    <ul class="benefit-list"><li>Strong Teeth</li><li>Fresh Breath</li><li>Whitening</li><li>Healthy Gums</li><li>Cavity</li><li>Tartar</li></ul>
    <div class="flavor-band">FRESH MINT BLAST</div>
  </section>

  <section class="box-face box-face--3">
    <div class="brand-name">Brivana</div>
    <div class="aloe-badge"><span class="aloe-badge__dot"></span><span class="aloe-badge__text">Extracts<br>of Aloe Vera</span></div>
    <div class="claim-band">FLUORIDE TOOTHPASTE WITH WHITENING MICRO PARTICLES</div>
    <div class="volume">100ml</div>
    <div class="mint-strip"><div class="mint-strip__seal" role="img" aria-label="Silver medical seal emblem"></div></div>
    <ul class="benefit-list"><li>Strong Teeth</li><li>Fresh Breath</li><li>Whitening</li><li>Healthy Gums</li><li>Cavity</li><li>Tartar</li></ul>
    <div class="flavor-band">FRESH MINT BLAST</div>
  </section>

  <section class="box-face box-face--4">
    <div class="brand-name">Brivana</div>
    <div class="aloe-badge"><span class="aloe-badge__dot"></span><span class="aloe-badge__text">Extracts<br>of Aloe Vera</span></div>
    <div class="claim-band">FLUORIDE TOOTHPASTE WITH WHITENING MICRO PARTICLES</div>
    <div class="volume">100ml</div>
    <div class="mint-strip"><div class="mint-strip__seal" role="img" aria-label="Silver medical seal emblem"></div></div>
    <ul class="benefit-list"><li>Strong Teeth</li><li>Fresh Breath</li><li>Whitening</li><li>Healthy Gums</li><li>Cavity</li><li>Tartar</li></ul>
    <div class="flavor-band">FRESH MINT BLAST</div>
  </section>
</div>
</body>
</html>
```